Simple design for eCommerce retailer of Custom Cut Mirror Frames

We need a fresh design for our eCommerce store. Currently, we need a design for each page on the existing site.

Here is the site as it stands right now: glassvela.com

Here is a competitor site that we like. The owner really likes the block look for the home page: framebloom.com

Here is a video we would like to feature: https://vidhost.example/kT7pQm2XrLa

Here is the color palate, emphasis on the green and purple: https://palettebox.example/quiet-evening-hues-theme-48213976/?showPublished=true

Here is an example of a landing page we are currently using: https://glassvela.com/lander-10-off-install/

Font for the site should be the google font Lato

Home page should include the following sections/blocks:

How it works
Shop now
Testimonials
Featured Products
Before and After Gallery
Updates

My team has been slow getting back to me with feedback. I'm pushing them to speed their process up.

Target Market(s)

Women, Ages 35-65+

Number of Pages Required

5+ page

Font styles to use
Sans Serif

Requirements
Must have
• -Before and after gallery
• -Star ratings
• -eCommerce look and feel
• -Info about being able to order free samples
• -Language from the checkmarks on the landing page
• -sleek product page
• -home page should be have a very modern design feel
Should not have
• Product Prices...the user has to use the calculator to determine the price of their purchase.
• Sliders

```html
<!DOCTYPE html>
<html lang="en">
<head>
<meta charset="utf-8">
<title>GlassVela – Home</title>
<link rel="stylesheet" href="https://fonts.googleapis.com/css2?family=Lato:wght@400;700&family=Lustria&display=swap">
<style>
:root{
  --board:#2d5752;
  --teal:#77aaa9;
  --teal-dark:#5f9392;
  --purple:#c39bcb;
  --purple-deep:#b085bd;
  --purple-pale:#f1e8f3;
  --ink:#333333;
  --muted:#7a7a7a;
  --line:#dddddd;
  --white:#ffffff;
  --star:#f2b01e;
  --sans:'Lato',Arial,sans-serif;
  --serif:'Lustria',Georgia,serif;
}
*{box-sizing:border-box;margin:0;padding:0}
html,body{width:1200px;height:3000px;overflow:hidden}
body{background:var(--board);font-family:var(--sans);color:var(--ink);position:relative}
.abs{position:absolute}
.wordmark{font-family:var(--serif);color:var(--white);text-align:center}
.board-logo{left:0;width:1200px;top:96px}
.board-logo .name{font-size:34px;display:flex;justify-content:center;align-items:center;gap:12px}
.board-logo .sq{width:22px;height:22px;background:var(--purple);display:inline-block}
.board-logo .tag{font-family:var(--sans);font-size:11px;letter-spacing:3px;margin-top:6px}
.thanks{left:0;width:1200px;top:2852px;font-size:40px;display:flex;justify-content:center;align-items:center;gap:14px}
.thanks .sq{width:26px;height:26px;background:var(--purple)}

.page{left:216px;top:216px;width:852px;height:2536px;background:var(--white)}
.promo{left:0;top:0;width:852px;height:20px;background:var(--teal);color:var(--white);font-size:9px;letter-spacing:1px;text-align:center;line-height:20px}
.site-logo{left:10px;top:42px}
.site-logo .name{font-family:var(--serif);font-size:22px;color:var(--teal-dark);display:flex;align-items:center;gap:8px}
.site-logo .sq{width:16px;height:16px;background:var(--purple)}
.site-logo .tag{font-size:7px;letter-spacing:1.6px;color:var(--teal-dark);margin-top:3px}
.consult{left:304px;top:40px;width:160px;font-size:8px;line-height:11px;color:var(--ink);text-align:right}
.consult b{color:var(--purple-deep);font-weight:400}
.pill{height:16px;border-radius:3px;font-size:8px;line-height:14px;text-align:center;top:42px}
.phone-pill{left:474px;width:94px;border:1px solid var(--line);color:var(--ink)}
.account-btn{left:584px;width:84px;background:var(--purple);color:var(--white);border:1px solid var(--purple)}
.cart-btn{left:680px;width:86px;border:1px solid var(--line);color:var(--muted)}
.main-nav{left:0;top:78px;width:852px;display:flex;justify-content:flex-end;gap:26px;padding-right:36px;font-size:8.5px;letter-spacing:.6px}
.main-nav span.active{color:var(--purple-deep);border-bottom:2px solid var(--purple);padding-bottom:6px}
.nav-rule{left:0;top:98px;width:852px;height:1px;background:var(--line)}

.hero{left:2px;top:114px;width:764px;height:364px;border:6px solid var(--teal);padding:6px}
.hero-photo{position:absolute;inset:6px;background:linear-gradient(100deg,#f4f2f0 0%,#e8e3dd 45%,#7a5b46 62%,#b9a797 75%,#5a4030 100%)}
.hero-title{left:68px;top:58px;font-family:var(--serif);font-size:38px;color:#3a3a3a}
.hero-title em{font-style:normal;color:var(--purple-deep)}
.hero-sub{left:60px;top:106px;font-size:9px;letter-spacing:3px;color:#555}
.btn{background:var(--purple);color:var(--white);font-size:9px;letter-spacing:.8px;text-align:center;border-radius:2px}
.hero-btn{left:124px;top:136px;width:104px;height:28px;line-height:28px}
.inset{left:48px;top:220px;width:202px;height:148px;background:var(--white);box-shadow:0 4px 10px rgba(0,0,0,.2);padding:6px}
.inset .ph{width:100%;height:110px;background:linear-gradient(120deg,#eceae6,#cfc7bd)}
.inset .cap{position:absolute;left:0;bottom:0;width:100%;height:30px;background:#2b2b2b;color:var(--white);font-family:var(--serif);font-size:11px;line-height:30px;padding-left:12px}
.swatch{left:224px;top:250px;width:80px;height:76px;background:var(--white);padding:5px;box-shadow:0 2px 6px rgba(0,0,0,.2)}
.swatch div{width:100%;height:100%;background:linear-gradient(135deg,#7a4e2a,#c89660,#5b3a1e)}

.section-title{left:0;width:852px;text-align:center;font-family:var(--serif);font-weight:400;font-size:30px;color:#2f2f2f}
.section-sub{left:0;width:852px;text-align:center;font-size:9px;letter-spacing:1.6px;color:#555}
.review{top:644px;width:196px;height:136px;border:1px solid #e6e6e6;box-shadow:0 2px 6px rgba(0,0,0,.08);padding:18px 16px 12px 22px;font-size:8px;line-height:14px;color:#666}
.review .q{color:#ccc;font-size:16px;font-family:var(--serif);position:absolute}
.review .stars{color:var(--star);font-size:10px;margin-top:8px;letter-spacing:1px}
.review .who{color:var(--teal-dark);font-size:8px}
.arrow{top:696px;width:18px;height:30px}

.video{left:2px;top:840px;width:456px;height:244px;background:linear-gradient(110deg,#cfd9e0 0%,#9fb0c2 40%,#3a4a7a 65%,#d8dde3 100%)}
.video .label{left:12px;top:12px;color:var(--white);font-size:9px;letter-spacing:1.4px}
.video .bar{left:0;bottom:0;width:456px;height:26px;background:rgba(0,0,0,.7)}
.slide{left:478px;top:840px;width:290px;height:244px;background:linear-gradient(135deg,#9fa8b2,#5e4a6a 55%,#c6ccd2)}
.slide .cap{left:0;top:164px;width:270px;height:48px;background:var(--white);font-family:var(--serif);font-size:11.5px;line-height:16px;color:#333;padding:8px 0 0 20px;text-align:center}
.slide .cap b{font-weight:400;color:var(--teal-dark)}
.note{left:658px;top:846px;width:314px;height:76px;background:var(--purple);border:1px solid var(--white);box-shadow:0 2px 8px rgba(0,0,0,.25);color:var(--white);font-size:11px;line-height:15px;text-align:center;padding:14px 18px}

.tile{top:1104px;width:240px;height:244px}
.tile-sample{left:2px;background:linear-gradient(135deg,#c8b8a8,#6a5444 60%,#e3dbd2)}
.tile-gallery{left:524px;background:linear-gradient(120deg,#5a3e2e,#d8c3a4 45%,#b39070)}
.tile .t{position:absolute;left:0;width:100%;bottom:34px;text-align:center;color:var(--white);font-family:var(--serif);font-size:19px}
.tile .b{position:absolute;left:58px;bottom:-6px;width:124px;height:24px;line-height:24px;background:var(--teal);color:var(--white);font-size:8.5px;text-align:center;letter-spacing:.6px}
.guarantee{left:262px;top:1104px;width:240px;height:244px;background:var(--purple-pale);text-align:center;padding:28px 24px}
.guarantee h3{font-family:var(--serif);font-weight:400;font-size:15px;line-height:19px;color:#333}
.guarantee p{font-size:8.5px;line-height:12px;color:#555;margin-top:8px}
.guarantee ul{list-style:none;text-align:left;margin:12px 0 0 28px;font-size:8px;line-height:22px;color:#555;letter-spacing:.6px}
.guarantee li svg{vertical-align:middle;margin-right:6px}
.guarantee .btn{width:80px;height:22px;line-height:22px;margin:6px auto 0}

.product{top:1484px;width:166px}
.product .frame{width:166px;height:134px;border:4px solid var(--teal);padding:10px;background:var(--white)}
.product.hover .frame{border-color:var(--purple)}
.product .frame div{width:100%;height:100%}
.product .n{text-align:center;font-family:var(--serif);font-size:15px;margin-top:14px;color:#2f2f2f}
.product.hover .n{color:var(--teal-dark)}
.product .s{text-align:center;font-size:8.5px;color:#666;margin-top:2px}
.product .st{text-align:center;color:var(--star);font-size:10px;letter-spacing:1px}
.product .btn{width:64px;height:22px;line-height:22px;margin:6px auto 0}
.product.hover .btn{background:var(--teal)}
.product .lk{text-align:center;font-size:7px;color:#777;text-decoration:underline;margin-top:6px}
.divider{left:0;top:1754px;width:852px;height:1px;background:var(--line)}
.outline-btn{border:1px solid var(--teal);background:var(--white);color:var(--ink);font-size:8.5px;text-align:center;letter-spacing:.6px}

.step{top:1928px;width:216px;height:156px;border:4px solid var(--purple);padding:4px}
.step .in{width:100%;height:100%;border:2px solid var(--teal);text-align:center;padding-top:26px}
.step .ic{width:40px;height:40px;margin:0 auto;background:#d5e6e5}
.step .k{font-size:8px;color:var(--teal-dark);margin-top:14px;letter-spacing:.6px}
.step .l{font-size:11px;letter-spacing:.8px;margin-top:2px}

.footer{left:0;top:2216px;width:852px;height:176px;background:var(--purple);border-top:4px solid var(--teal);border-bottom:4px solid var(--teal);color:var(--white)}
.fcol{top:22px}
.fcol h4{font-family:var(--serif);font-weight:400;font-size:15px;margin-bottom:10px}
.fcol div{font-size:8px;line-height:15px}
.fcol svg{vertical-align:middle;margin-right:5px}
.f-input{left:590px;top:50px;width:176px;height:26px;background:var(--white);color:#999;font-size:8px;line-height:26px;padding-left:8px}
.f-join{left:590px;top:84px;width:82px;height:24px;line-height:24px;background:var(--teal);color:var(--white);font-size:8px;text-align:center}

.lower .cr{font-size:7.5px;line-height:11px;color:#666;text-align:center}
.badge{top:2428px;width:62px;height:48px;background:#e9e9e9;border:1px solid #ccc}
.links div{font-size:8px;line-height:16px;color:#555}
.lh{font-family:var(--serif);font-size:15px;color:var(--purple-deep)}
.soc{width:16px;height:16px;border:1px solid #bbb;border-radius:50%;display:inline-block;margin-right:6px}
.card{width:24px;height:15px;border:1px solid #ccc;border-radius:2px;display:inline-block;margin-right:4px;background:#f3f3f3}
</style>
</head>
<body>

<div class="abs wordmark board-logo">
  <div class="name"><span class="sq"></span>GlassVela</div>
  <div class="tag">CUSTOM FRAMES FOR EVERY MIRROR</div>
</div>

<main class="abs page">
  <div class="abs promo">GET UP TO 7 SAMPLES FREE! USE CODE <b>FREESAMPLE</b> AT CHECKOUT</div>

  <header>
    <div class="abs site-logo">
      <div class="name"><span class="sq"></span>GlassVela</div>
      <div class="tag">CUSTOM FRAMES FOR EVERY MIRROR</div>
    </div>
    <div class="abs consult">Near Rivermoor Or Its Valley Towns?<br><b>Free In-Home Consultation</b></div>
    <div class="abs pill phone-pill">(555) 014-2276</div>
    <div class="abs pill account-btn">My Account</div>
    <div class="abs pill cart-btn">My Cart (0)</div>
    <nav class="abs main-nav">
      <span class="active">HOME</span><span>SHOP MIRROR FRAMES</span><span>CUSTOM FRAMED MIRRORS</span><span>HOW IT WORKS</span><span>BEFORE &amp; AFTER GALLERY</span><span>CONTACT US</span>
    </nav>
    <div class="abs nav-rule"></div>
  </header>

  <section class="abs hero">
    <div class="hero-photo" role="img" aria-label="Bathroom vanity with a white vessel sink and a bronze framed mirror"></div>
    <div class="abs hero-title">Look <em>C</em>lassy</div>
    <div class="abs hero-sub">FIT EVERY BATHROOM PERFECTLY</div>
    <div class="abs btn hero-btn">SHOP NOW</div>
    <div class="abs inset">
      <div class="ph" role="img" aria-label="Close view of the sink with the framed mirror"></div>
      <div class="cap">Seacliff Bronze Brown Frame</div>
    </div>
    <div class="abs swatch"><div role="img" aria-label="Bronze brown frame corner sample"></div></div>
  </section>

  <section>
    <h2 class="abs section-title" style="top:560px">Our Customer Reviews</h2>
    <div class="abs section-sub" style="top:602px">OVER 2500+ SATISFIED CUSTOMERS 5 STAR REVIEWS</div>
    <svg class="abs arrow" style="left:0" viewBox="0 0 18 30"><path d="M14 3 3 15l11 12" fill="none" stroke="#bbb" stroke-width="2"/></svg>
    <svg class="abs arrow" style="left:750px" viewBox="0 0 18 30"><path d="M4 3l11 12L4 27" fill="none" stroke="#bbb" stroke-width="2"/></svg>
    <div class="abs review" style="left:58px"><span class="q" style="left:8px;top:10px">“</span>Great product and great service! Adding frames to our mirrors made all the difference in how the master bath looks. You can't beat this for the money!<div class="stars">★★★★★</div><div class="who">Karen D., Oakridge, Ca</div></div>
    <div class="abs review" style="left:288px"><span class="q" style="left:8px;top:10px">“</span>We were so happy with the first two frames we purchased, we ordered a frame for our other bathroom. I would highly recommend this company.<div class="stars">★★★★★</div><div class="who">Lena M., Pinevale, Ca</div></div>
    <div class="abs review" style="left:508px"><span class="q" style="left:8px;top:10px">“</span>I did two bathrooms and couldn't be happier. What a difference the new frames made! Do yourself a favor and frame your mirrors.<div class="stars">★★★★★</div><div class="who">Carla T., Brookfield, Ca</div></div>
  </section>

  <section>
    <div class="abs video" role="img" aria-label="Video still of a woman fitting a frame onto a bathroom mirror">
      <div class="abs label">SEE HOW EASY IT IS</div>
      <svg class="abs" style="left:204px;top:96px" width="44" height="44" viewBox="0 0 44 44"><circle cx="22" cy="22" r="22" fill="#b085bd"/><path d="M17 13v18l14-9z" fill="#fff"/></svg>
      <div class="abs bar">
        <svg width="456" height="26" viewBox="0 0 456 26"><rect x="10" y="4" width="436" height="2" fill="#888"/><rect x="10" y="4" width="120" height="2" fill="#fff"/><path d="M12 11h3v9h-3zM18 11h3v9h-3z" fill="#fff"/><path d="M30 11v9l-6-4.5zM44 11v9l6-4.5z" fill="#fff"/><rect x="400" y="12" width="10" height="8" fill="none" stroke="#fff"/><rect x="420" y="12" width="12" height="8" fill="none" stroke="#fff"/></svg>
      </div>
    </div>
    <div class="abs slide" role="img" aria-label="Hands wiping a mirror frame clean">
      <div class="abs cap">No Tools Complete <b>Fitting Frame</b>,<br>so you don't need any room around it</div>
    </div>
    <div class="abs note">This is Slider Pictures Where Each Images and Features Automatically Slides and Changes after Every 5 Seconds</div>
  </section>

  <section>
    <div class="abs tile tile-sample" role="img" aria-label="Stack of frame corner samples">
      <div class="t">Order A Free Sample</div><div class="b">GET SAMPLE NOW</div>
    </div>
    <div class="abs guarantee">
      <h3>100% Satisfaction<br>Guarantee!</h3>
      <p>Unsure? - Don't Worry, We Will Walk you Through Every Step of the Process.</p>
      <ul>
        <li><svg width="10" height="10" viewBox="0 0 10 10"><circle cx="5" cy="5" r="4.5" fill="none" stroke="#888"/><path d="M3 5l1.5 1.5L7 3.5" fill="none" stroke="#888"/></svg>GUARANTEED TO FIT</li>
        <li><svg width="10" height="10" viewBox="0 0 10 10"><circle cx="5" cy="5" r="4.5" fill="none" stroke="#888"/><path d="M3 5l1.5 1.5L7 3.5" fill="none" stroke="#888"/></svg>INSTALLS IN MINUTES</li>
        <li><svg width="10" height="10" viewBox="0 0 10 10"><circle cx="5" cy="5" r="4.5" fill="none" stroke="#888"/><path d="M3 5l1.5 1.5L7 3.5" fill="none" stroke="#888"/></svg>WE HAVE YOU COVERED!</li>
      </ul>
      <div class="btn">SHOP NOW</div>
    </div>
    <div class="abs tile tile-gallery" role="img" aria-label="Bathroom before and after a framed mirror, split view">
      <svg class="abs" style="left:108px;top:80px" width="24" height="24" viewBox="0 0 24 24"><circle cx="12" cy="12" r="11" fill="#fff"/><path d="M10 8l-4 4 4 4M14 8l4 4-4 4" fill="none" stroke="#555" stroke-width="1.5"/></svg>
      <div class="t">Before/After Gallery</div><div class="b">VIEW ALL GALLERY</div>
    </div>
  </section>

  <section>
    <h2 class="abs section-title" style="top:1408px">Featured Products</h2>
    <div class="abs section-sub" style="top:1448px">EXPLORE THE WIDE RANGE OF THE CUSTOM DESIGNED FRAMES</div>
    <div class="abs product" style="left:2px">
      <div class="frame"><div role="img" aria-label="Contemporary silver frame corner" style="background:linear-gradient(135deg,#7d7a70,#c9c4b4 50%,#8a8678)"></div></div>
      <div class="n">Contempory Silver</div><div class="s">Modern Look</div><div class="st">★★★★★</div><div class="btn">SHOP NOW</div><div class="lk">Shop All Frames</div>
    </div>
    <div class="abs product hover" style="left:202px">
      <div class="frame"><div role="img" aria-label="Black silver frame corner" style="background:linear-gradient(135deg,#3c3c3c,#8a9a9a 50%,#9ec4c3)"></div></div>
      <div class="n">Seacliff Black Silver</div><div class="s">Versatile Look</div><div class="st">★★★★★</div><div class="btn">SHOP NOW</div><div class="lk">Shop All Frames</div>
    </div>
    <div class="abs product" style="left:400px">
      <div class="frame"><div role="img" aria-label="Espresso frame corner" style="background:linear-gradient(135deg,#2a1c16,#4a3328 50%,#20140f)"></div></div>
      <div class="n">Harbor Espresso</div><div class="s">Modern Look</div><div class="st">★★★★★</div><div class="btn">SHOP NOW</div><div class="lk">Shop All Frames</div>
    </div>
    <div class="abs product" style="left:600px">
      <div class="frame"><div role="img" aria-label="Java brown frame corner" style="background:linear-gradient(135deg,#6a3d1e,#b4763e 50%,#5a3218)"></div></div>
      <div class="n">Harbor Java</div><div class="s">Modern Look</div><div class="st">★★★★★</div><div class="btn">SHOP NOW</div><div class="lk">Shop All Frames</div>
    </div>
    <div class="abs divider"></div>
    <div class="abs outline-btn" style="left:360px;top:1772px;width:132px;height:28px;line-height:26px">VIEW ALL FRAMES</div>
  </section>

  <section>
    <h2 class="abs section-title" style="top:1846px">How it Works</h2>
    <div class="abs section-sub" style="top:1888px">QUICK, EASY, &amp; AFFORDABLE CUSTOM FRAMES</div>
    <div class="abs step" style="left:2px"><div class="in"><div class="ic" role="img" aria-label="Ruler and pencil icon"></div><div class="k">STEP 01</div><div class="l">MEASURE YOUR MIRROR</div></div></div>
    <div class="abs step" style="left:274px"><div class="in"><div class="ic" role="img" aria-label="Frame corner icon"></div><div class="k">STEP 02</div><div class="l">CHOOSE A FRAME</div></div></div>
    <div class="abs step" style="left:548px"><div class="in"><div class="ic" role="img" aria-label="Framed mirror installation icon"></div><div class="k">STEP 03</div><div class="l">EASY FINE INSTALLATION</div></div></div>
    <div class="abs" style="left:324px;top:2120px;width:124px;height:32px;line-height:32px;background:var(--teal);color:var(--white);font-size:9px;text-align:center;letter-spacing:.6px">GET START NOW</div>
  </section>

  <footer class="abs footer">
    <div class="abs fcol" style="left:2px">
      <h4>Contact us</h4>
      <div><svg width="8" height="10" viewBox="0 0 8 10"><path d="M4 10S0 5.5 0 4a4 4 0 018 0c0 1.5-4 6-4 6z" fill="#fff"/><circle cx="4" cy="4" r="1.5" fill="#c39bcb"/></svg>12 Alder Lane, Suite B,<br>&nbsp;&nbsp;&nbsp;&nbsp;Rivermoor, CA 90000</div>
      <div style="margin-top:6px"><svg width="8" height="10" viewBox="0 0 8 10"><rect x="1" y="0" width="6" height="10" rx="1" fill="#fff"/></svg>(555) 014-2276</div>
      <div style="margin-top:6px"><svg width="10" height="8" viewBox="0 0 10 8"><rect width="10" height="8" fill="#fff"/><path d="M0 0l5 4 5-4" fill="none" stroke="#c39bcb"/></svg>support@glassvela.com</div>
    </div>
    <div class="abs fcol" style="left:170px"><h4>My Account</h4><div>My Account<br>My Cart<br>Login / Sign up<br>Track my Order<br>Support</div></div>
    <div class="abs fcol" style="left:294px"><h4>Quick Links</h4><div>Shop Mirror Frames<br>Custom Framed Mirrors<br>How It Works<br>Before &amp; After Gallery<br>Contact us</div></div>
    <div class="abs fcol" style="left:450px"><h4>Company</h4><div>Privacy Policy<br>Terms &amp; Conditions<br>Security &amp; Our Site<br>Our Guarantee<br>Product Care</div></div>
    <div class="abs fcol" style="left:590px"><h4>Save <span style="font-family:var(--sans);font-size:11px">10%</span> OFF now!</h4></div>
    <div class="abs f-input">Enter your email...</div>
    <div class="abs f-join">JOIN NOW</div>
  </footer>

  <div class="lower">
    <div class="abs" style="left:10px;top:2426px">
      <div class="site-logo" style="position:static"><div class="name"><span class="sq"></span>GlassVela</div><div class="tag">CUSTOM FRAMES FOR EVERY MIRROR</div></div>
      <div class="cr" style="margin-top:6px">© Copyright 2019. GlassVela.com<br>All Rights Reserved</div>
    </div>
    <div class="abs badge" style="left:184px"></div>
    <div class="abs badge" style="left:252px"></div>
    <div class="abs links" style="left:350px;top:2424px"><div>FAQ<br>Customer Support<br>Contact us<br>Shipping</div></div>
    <div class="abs" style="left:474px;top:2420px"><div class="lh">Follow us</div><div style="margin-top:8px"><span class="soc"></span><span class="soc"></span><span class="soc"></span><span class="soc"></span></div></div>
    <div class="abs" style="left:628px;top:2420px"><div class="lh">We Accept</div><div style="margin-top:8px"><span class="card"></span><span class="card"></span><span class="card"></span><span class="card"></span><span class="card"></span></div></div>
  </div>
</main>

<div class="abs wordmark thanks"><span class="sq"></span>Thank You</div>

</body>
</html>
```